Name card design for KORU mobile accessories company

KORU is an upmarket brand, we are looking for professional business card design.

the design should be neat and simple but giving a strong feeling.
should not be colorful. make it black/white/gray tone

Name:
Job title:
Contact no.:
company address: i would like the company address to be very small and thin.
link to social media profile:
company website:

*the company have no website yet
as the project is done please i also would like the font that use in design as well; for more further people in company need a business card:)
Updates

Thank you for all super fast submission :D they're all look cool!

i have just update my brief to make the statement clearer, please check it out :)
if you have any question please dont hesitate to ask.
i would like see more design from you! 
Keep it up!  :D

Target Market(s)

Company target are upmarket company distributor, such as Velmora and Quill store.

Industry/Entity Type

Business

Font styles to use
Serif
Sans Serif
Other font styles liked:
• Formal and mordern

Colors
ffffff
eeeeee
d3d3d3
919191
474747
1b1b1b
000000
333333

Requirements
Must have
• The design must be professional clean and clear but also Strong and Modern!
text should be formal and mordern
Should not have
• No complicated design!

```html
<!DOCTYPE html>
<html lang="en">
<head>
<meta charset="UTF-8">
<title>KORU – Business Card</title>
<link rel="stylesheet" href="https://fonts.googleapis.com/css2?family=Outfit:wght@600;700&family=Arimo:wght@400&family=Raleway:wght@300&display=swap">
<style>
  :root {
    --card-bg: #e3e3e3;
    --card-bg-edge: #d9d9d9;
    --ink: #1b1b1b;
    --ink-black: #000000;
    --muted: #a9a9a9;
    --label: #bdbdbd;
    --address: #a3a3a3;
  }
  html, body {
    margin: 0;
    padding: 0;
    width: 1200px;
    height: 686px;
    overflow: hidden;
    background: var(--card-bg);
  }
  .card {
    position: relative;
    width: 1200px;
    height: 686px;
    overflow: hidden;
    background: radial-gradient(ellipse at 40% 40%, var(--card-bg) 0%, var(--card-bg-edge) 100%);
  }
  .holder-name {
    position: absolute;
    left: 130px;
    top: 128px;
    margin: 0;
    font-family: "Outfit", sans-serif;
    font-weight: 600;
    font-size: 78px;
    line-height: 1;
    letter-spacing: -1px;
    color: var(--ink);
  }
  .holder-title {
    position: absolute;
    left: 130px;
    top: 206px;
    margin: 0;
    font-family: "Outfit", sans-serif;
    font-weight: 700;
    font-style: italic;
    font-size: 30px;
    line-height: 1;
    color: var(--muted);
  }
  .contact-list {
    position: absolute;
    left: 125px;
    top: 294px;
    margin: 0;
    padding: 0;
    list-style: none;
    font-family: "Arimo", sans-serif;
    font-size: 35px;
    line-height: 42px;
    color: var(--ink);
  }
  .contact-label {
    color: var(--label);
  }
  .company-address {
    position: absolute;
    left: 125px;
    top: 486px;
    margin: 0;
    font-style: normal;
    font-family: "Raleway", sans-serif;
    font-weight: 300;
    font-size: 23px;
    line-height: 30px;
    color: var(--address);
  }
  .brand-name {
    position: absolute;
    left: 797px;
    top: 505px;
    width: 310px;
    height: 108px;
    margin: 0;
    display: flex;
    align-items: center;
    justify-content: center;
    font-family: "Outfit", sans-serif;
    font-weight: 600;
    font-size: 104px;
    line-height: 1;
    letter-spacing: 2px;
    color: var(--ink-black);
  }
</style>
</head>
<body>
  <main class="card">
    <h1 class="holder-name">Daniel Varek</h1>
    <p class="holder-title">General Manager</p>

    <ul class="contact-list">
      <li><span class="contact-label">phone : </span>482-719305</li>
      <li><span class="contact-label">email : </span>daniel@korumail.com</li>
      <li><span class="contact-label">link : </span>www.socialnet.com/koru</li>
      <li><span class="contact-label">website : </span>www.koru.com</li>
    </ul>

    <address class="company-address">
      214 Marena Ave.12 st.<br>
      Stone Blv<br>
      Delvar, HN<br>
      00718
    </address>

    <p class="brand-name">KORU</p>
  </main>
</body>
</html>
```